Corvelle Strategies business card

I need a business card for my new strategic consulting LLC, Corvelle Strategies. We specialize in helping people who care about broadband technology and telecommunications policy, and we're based in Washington DC. I'm looking for a card that says smart, credible, future-facing and signals a high level of expertise. It's DC, so there's clearly a limit to how crazy we can go with this card, but I am looking for a design that reflects a company that is comfortable with technology, policy, and having a little bit fun. I'm uploading my logo below, and I'd like to have it be part of the card design in some fashion.
Target Market(s)
Telecommunications and technology policy professionals
Industry/Entity Type
Technology policy
Contact Information for Business Card
Name of business, my name (Glen Mosswater), email (glen@corvellestrategies-example.com) , phone number (202-555-0148)phone number

```html
<!DOCTYPE html>
<html lang="en">
<head>
<meta charset="utf-8">
<title>Corvelle Strategies business card</title>
<link rel="stylesheet" href="https://fonts.googleapis.com/css2?family=Lato:wght@400;700;900&display=swap">
<style>
  :root {
    --brand-blue: #1559a3;
    --deep-blue: #0a4a87;
    --sun-gold: #fbb040;
    --ink: #2b2b2b;
    --paper: #ffffff;
    --backdrop: #9a9a9a;
  }
  * { box-sizing: border-box; margin: 0; padding: 0; }
  html, body {
    width: 1200px; height: 1059px; overflow: hidden;
    background: var(--backdrop);
    font-family: "Lato", sans-serif;
  }
  .card {
    position: absolute;
    left: 254px;
    width: 706px; height: 403px;
    border-radius: 28px;
    overflow: hidden;
  }
  .card-front { top: 82px; background: var(--paper); }
  .card-back { top: 569px; background: var(--deep-blue); }

  .wordmark {
    position: absolute;
    left: 0; right: 0;
    display: flex; align-items: center; justify-content: center; gap: 16px;
    font-weight: 900;
    font-size: 54px;
    letter-spacing: -0.5px;
    line-height: 1;
  }
  .card-front .wordmark { top: 100px; color: var(--brand-blue); }
  .card-back .wordmark { top: 174px; color: var(--paper); }
  .wordmark-dot {
    width: 34px; height: 34px; border-radius: 50%;
    background: var(--sun-gold);
    flex: none;
  }

  .holder {
    position: absolute;
    right: calc(706px - 284px);
    top: 228px;
    text-align: right;
  }
  .holder-name {
    font-weight: 700; font-size: 28px; color: var(--brand-blue);
    white-space: nowrap;
  }
  .holder-role {
    font-weight: 400; font-size: 18px; color: var(--ink);
    margin-top: 6px; letter-spacing: 0.5px;
  }
  .divider {
    position: absolute; left: 307px; top: 226px;
    width: 2px; height: 74px; background: var(--brand-blue);
  }
  .contact {
    position: absolute; left: 328px; top: 231px;
    list-style: none;
  }
  .contact-item {
    display: flex; align-items: center; gap: 12px;
    font-size: 18px; color: var(--ink);
    height: 24px; margin-bottom: 11px;
    white-space: nowrap;
  }
  .contact-icon { width: 24px; height: 20px; flex: none; fill: var(--brand-blue); }

  .edge-band {
    position: absolute; left: 0; bottom: 0;
    width: 706px; height: 16px; display: block;
  }
</style>
</head>
<body>
  <section class="card card-front" aria-label="Card front">
    <div class="wordmark"><span>Corvelle Strategies</span><span class="wordmark-dot"></span></div>

    <div class="holder">
      <div class="holder-name">Glen Mosswater</div>
      <div class="holder-role">Owner</div>
    </div>
    <div class="divider"></div>
    <ul class="contact">
      <li class="contact-item">
        <svg class="contact-icon" viewBox="0 0 24 24" aria-hidden="true">
          <path d="M6.6 10.8a15 15 0 0 0 6.6 6.6l2.2-2.2c.3-.3.7-.4 1-.2 1.1.4 2.3.6 3.6.6.6 0 1 .4 1 1V20c0 .6-.4 1-1 1C10.6 21 3 13.4 3 4c0-.6.4-1 1-1h3.5c.6 0 1 .4 1 1 0 1.3.2 2.5.6 3.6.1.3 0 .7-.2 1z"/>
        </svg>
        <span>(202-555-0148)</span>
      </li>
      <li class="contact-item">
        <svg class="contact-icon" viewBox="0 0 24 20" aria-hidden="true">
          <path d="M1 2h22v16H1z M1 2l11 8 11-8" fill="var(--brand-blue)"/>
          <path d="M2 3l10 7.5L22 3" fill="none" stroke="#fff" stroke-width="1.8"/>
        </svg>
        <span>glen@corvellestrategies-example.com</span>
      </li>
    </ul>

    <svg class="edge-band" viewBox="0 0 706 16" preserveAspectRatio="none" aria-hidden="true">
      <polygon points="0,0 360,0 340,16 0,16" fill="var(--sun-gold)"/>
      <polygon points="372,0 706,0 706,16 350,16" fill="var(--brand-blue)"/>
    </svg>
  </section>

  <section class="card card-back" aria-label="Card back">
    <div class="wordmark"><span>Corvelle Strategies</span><span class="wordmark-dot"></span></div>
  </section>
</body>
</html>
```